Print & Packaging Design for Snug Pip Teething & Healing Necklaces

Bring your Creative Juices this-a way! Smart, savvy, up-market business needs a logo & swing tags! Do you have what it takes?

```html
<!DOCTYPE html>
<html lang="en">
<head>
<meta charset="utf-8">
<title>Snug Pip – Swing Tags</title>
<link rel="stylesheet" href="https://fonts.googleapis.com/css2?family=Fredoka:wght@600&family=Courgette&display=swap">
<style>
  :root {
    --page-bg: #ededed;
    --tag-blue: #8fd3e8;
    --brand-navy: #1f4f93;
    --copy-navy: #25324a;
    --accent-yellow: #f6bd1e;
    --grommet-ring: #c9cdd1;
    --grommet-hole: #f4f6f7;
    --photo-light: #f3e4dc;
    --photo-mid: #e0c2b0;
    --photo-shadow: #b89a8a;
  }
  * { margin: 0; padding: 0; box-sizing: border-box; }
  html, body {
    width: 1200px;
    height: 800px;
    overflow: hidden;
    background: var(--page-bg);
  }
  .canvas {
    position: relative;
    width: 1200px;
    height: 800px;
  }
  .tag {
    position: absolute;
    top: 22px;
    height: 734px;
  }
  .tag--front { left: 262px; width: 290px; }
  .tag--back  { left: 610px; width: 340px; }
  .tag__shape {
    position: absolute;
    inset: 0;
    width: 100%;
    height: 100%;
  }
  .tag__body { fill: var(--tag-blue); }
  .grommet__ring { fill: var(--grommet-ring); }
  .grommet__hole { fill: var(--grommet-hole); }

  .brand {
    position: absolute;
    left: 0;
    right: 0;
    text-align: center;
  }
  .brand__mark {
    display: block;
    width: 46px;
    height: 46px;
    margin: 0 auto 6px;
    border-radius: 50%;
    background: var(--accent-yellow);
  }
  .brand__name {
    font-family: "Fredoka", sans-serif;
    font-weight: 600;
    font-size: 52px;
    line-height: 1;
    color: var(--brand-navy);
  }
  .brand__tagline {
    margin-top: 8px;
    font-family: "Courgette", cursive;
    font-size: 18px;
    color: var(--copy-navy);
  }
  .tag--front .brand { top: 378px; }
  .tag--back .brand  { top: 92px; }

  .benefits {
    position: absolute;
    top: 372px;
    left: 18px;
    right: 18px;
    list-style: none;
    text-align: center;
    font-family: "Courgette", cursive;
    font-size: 18px;
    line-height: 31px;
    color: var(--copy-navy);
  }
</style>
</head>
<body>
<main class="canvas">

  <section class="tag tag--front" aria-label="Swing tag front">
    <svg class="tag__shape" viewBox="0 0 300 730" preserveAspectRatio="none">
      <defs>
        <linearGradient id="photo-tones" x1="0" y1="0" x2="0.4" y2="1">
          <stop offset="0" stop-color="var(--photo-light)"/>
          <stop offset="0.6" stop-color="var(--photo-mid)"/>
          <stop offset="1" stop-color="var(--photo-shadow)"/>
        </linearGradient>
      </defs>
      <g class="tag__body">
        <rect x="0" y="300" width="300" height="300" rx="95"/>
        <rect x="28" y="500" width="244" height="230" rx="44"/>
      </g>
      <g role="img" aria-label="Photo of a smiling baby in a striped knit hat wearing an amber teething necklace">
        <circle cx="62" cy="62" r="52" fill="url(#photo-tones)"/>
        <circle cx="238" cy="62" r="52" fill="url(#photo-tones)"/>
        <ellipse cx="150" cy="185" rx="130" ry="140" fill="url(#photo-tones)"/>
      </g>
      <g class="grommet">
        <circle class="grommet__ring" cx="150" cy="694" r="17"/>
        <circle class="grommet__hole" cx="150" cy="694" r="10"/>
      </g>
    </svg>
    <div class="brand">
      <span class="brand__mark" aria-hidden="true"></span>
      <div class="brand__name">Snug Pip</div>
      <div class="brand__tagline">teething &amp; healing necklaces</div>
    </div>
  </section>

  <section class="tag tag--back" aria-label="Swing tag back">
    <svg class="tag__shape" viewBox="0 0 300 730" preserveAspectRatio="none">
      <g class="tag__body">
        <circle cx="62" cy="62" r="52"/>
        <circle cx="238" cy="62" r="52"/>
        <ellipse cx="150" cy="185" rx="130" ry="140"/>
        <rect x="0" y="300" width="300" height="300" rx="95"/>
        <rect x="28" y="500" width="244" height="230" rx="44"/>
      </g>
      <g class="grommet">
        <circle class="grommet__ring" cx="150" cy="694" r="15"/>
        <circle class="grommet__hole" cx="150" cy="694" r="9"/>
      </g>
    </svg>
    <div class="brand">
      <span class="brand__mark" aria-hidden="true"></span>
      <div class="brand__name">Snug Pip</div>
      <div class="brand__tagline">teething &amp; healing necklaces</div>
    </div>
    <ul class="benefits">
      <li>- natural pain relief for your babe.</li>
      <li>- relieve your babes pain and sleep better at night.</li>
      <li>- sleep better at night knowing you've helped to ease your babes pain.</li>
      <li>- baltic amber teething necklaces.</li>
      <li>- gemstone nursing necklaces.</li>
      <li>- fertility and birthing jewellery.</li>
      <li>- natural healing jewellery.</li>
    </ul>
  </section>

</main>
</body>
</html>
```